Unique malt liquor beverage needs a logo design and bottle (6.9oz clear glass flask) label designed.

We need a logo and bottle label design for our new beverage here at Brightwell Drinks, a new company based in West Virginia. This is a differentiated product in that we use only natural ingredients and deliver it in a novel 6.9oz glass flask. Our new beverage is a naturally flavored malt liquor drink that we call "Tumbler". Our proposed tag line will be "Made to Tumble" or "Bold Tip. Quick Tumble". We want a logo and bottle label design that differentiates us even further.

Target Market(s)

See images I uploaded to see our two competitors...we need to be better than this but it gives you idea of the spirit of this beverage class.

Industry/Entity Type

Alcohol beverage

Requirements
Must have
• Label needs to include “14% alc/vol 6.9 oz” Both of these elements can be small and at bottom of front face of label. Also must look great on clear glass flask.
Should not have
• Do not put "malt liquor" on label. Under "Tumbler" name it will need to state "Alcoholic Beverage"

```html
<!DOCTYPE html>
<html lang="en">
<head>
<meta charset="UTF-8">
<title>Tumbler – Front Label</title>
<link href="https://fonts.googleapis.com/css2?family=Playfair+Display:wght@700;900&family=Fjalla+One&family=Pinyon+Script&family=Rye&family=Josefin+Sans:wght@600&display=swap" rel="stylesheet">
<style>
  :root {
    --page: #efedea;
    --label: #7b3b33;
    --label-deep: #6c322b;
    --ornament: #8c4a40;
    --line: #c9a99c;
    --silver: #e4e4e4;
    --silver-shade: #8f8f8f;
    --ink: #1e1414;
    --gold: #d9a45a;
    --blush: #e8c4bd;
    --pink: #e7b7b4;
  }
  * { margin: 0; padding: 0; box-sizing: border-box; }
  html, body { width: 1023px; height: 1200px; overflow: hidden; background: var(--page); }
  .canvas { position: relative; width: 1023px; height: 1200px; }

  .label {
    position: absolute; left: 100px; top: 100px; width: 823px; height: 1000px;
    background: var(--label); border-radius: 46px;
    box-shadow: 0 2px 10px rgba(0,0,0,.12);
    overflow: hidden;
  }
  .label-frame { position: absolute; inset: 0; }

  .ornament { position: absolute; background: var(--ornament); }
  .ornament-top { left: 300px; top: 26px; width: 223px; height: 170px; border-radius: 0 0 110px 110px; }
  .ornament-corner-tl { left: 28px; top: 28px; width: 170px; height: 250px; border-radius: 20px 20px 90px 20px; }
  .ornament-corner-tr { right: 28px; top: 28px; width: 170px; height: 250px; border-radius: 20px 20px 20px 90px; }
  .ornament-side-l { left: 20px; top: 440px; width: 70px; height: 170px; border-radius: 35px; }
  .ornament-side-r { right: 20px; top: 440px; width: 70px; height: 170px; border-radius: 35px; }
  .ornament-corner-bl { left: 28px; bottom: 70px; width: 130px; height: 180px; border-radius: 20px 80px 20px 20px; }
  .ornament-corner-br { right: 28px; bottom: 70px; width: 130px; height: 180px; border-radius: 80px 20px 20px 20px; }
  .ornament-bottom { left: 330px; bottom: 24px; width: 163px; height: 46px; border-radius: 80px 80px 0 0; }
  .flourish { left: 200px; top: 392px; width: 423px; height: 52px; border-radius: 26px; background: var(--label-deep); }

  .maker {
    position: absolute; left: 0; right: 0; top: 252px;
    display: flex; justify-content: center; align-items: center; gap: 14px;
    font-family: "Playfair Display", serif; font-weight: 700;
    font-size: 34px; letter-spacing: 1px; color: var(--blush);
  }
  .maker-dot { width: 16px; height: 16px; border-radius: 50%; background: var(--blush); }

  .product-name {
    position: absolute; left: 0; right: 0; top: 455px; text-align: center;
    font-family: "Playfair Display", serif; font-weight: 900;
    font-size: 108px; line-height: 1; letter-spacing: 2px;
    color: var(--silver);
    text-shadow: 3px 3px 0 var(--ink), 1px 1px 0 var(--silver-shade);
  }
  .tagline {
    position: absolute; left: 0; right: 0; top: 588px; text-align: center;
    font-family: "Fjalla One", sans-serif; font-size: 52px; line-height: 1;
    letter-spacing: 1px; color: var(--gold);
  }
  .flavor-note {
    position: absolute; left: 0; right: 0; top: 660px; text-align: center;
    font-family: "Pinyon Script", cursive; font-size: 70px; line-height: 1.1;
    color: var(--blush);
  }
  .category {
    position: absolute; left: 0; right: 0; top: 772px; text-align: center;
    font-family: "Rye", serif; font-size: 34px; line-height: 1;
    letter-spacing: 1px;
    color: var(--pink); text-shadow: 2px 2px 0 var(--ink);
  }
  .origin {
    position: absolute; left: 0; right: 0; top: 836px; text-align: center;
    font-family: "Josefin Sans", sans-serif; font-weight: 600;
    font-size: 28px; letter-spacing: 9px; color: var(--ink);
  }
  .volume {
    position: absolute; left: 0; right: 0; top: 888px; text-align: center;
    font-family: "Josefin Sans", sans-serif; font-weight: 600;
    font-size: 18px; letter-spacing: 2px; color: var(--blush);
  }
</style>
</head>
<body>
<main class="canvas">
  <section class="label">
    <div class="ornament ornament-top" role="img" aria-label="Art deco flower with fanned leaves"></div>
    <div class="ornament ornament-corner-tl" role="img" aria-label="Scrolled column corner with leaves"></div>
    <div class="ornament ornament-corner-tr" role="img" aria-label="Scrolled column corner with leaves"></div>
    <div class="ornament ornament-side-l" role="img" aria-label="Side flower ornament"></div>
    <div class="ornament ornament-side-r" role="img" aria-label="Side flower ornament"></div>
    <div class="ornament ornament-corner-bl" role="img" aria-label="Scroll and leaf cluster"></div>
    <div class="ornament ornament-corner-br" role="img" aria-label="Scroll and leaf cluster"></div>
    <div class="ornament ornament-bottom" role="img" aria-label="Small fanned leaf motif"></div>
    <div class="ornament flourish" role="img" aria-label="Decorative swirl flourish"></div>

    <svg class="label-frame" width="823" height="1000" viewBox="0 0 823 1000" aria-hidden="true">
      <rect x="14" y="14" width="795" height="972" rx="36" fill="none" stroke="var(--line)" stroke-width="3" stroke-dasharray="2 7" stroke-linecap="round"/>
      <rect x="24" y="24" width="775" height="952" rx="30" fill="none" stroke="var(--line)" stroke-width="1.5"/>
      <g stroke="var(--line)" stroke-width="1.5">
        <line x1="200" y1="70" x2="300" y2="70"/><line x1="200" y1="82" x2="300" y2="82"/>
        <line x1="200" y1="94" x2="300" y2="94"/><line x1="200" y1="106" x2="300" y2="106"/>
        <line x1="523" y1="70" x2="623" y2="70"/><line x1="523" y1="82" x2="623" y2="82"/>
        <line x1="523" y1="94" x2="623" y2="94"/><line x1="523" y1="106" x2="623" y2="106"/>
        <line x1="44" y1="290" x2="44" y2="740"/><line x1="56" y1="290" x2="56" y2="740"/>
        <line x1="779" y1="290" x2="779" y2="740"/><line x1="767" y1="290" x2="767" y2="740"/>
        <line x1="180" y1="944" x2="320" y2="944"/><line x1="180" y1="956" x2="320" y2="956"/>
        <line x1="503" y1="944" x2="643" y2="944"/><line x1="503" y1="956" x2="643" y2="956"/>
      </g>
    </svg>

    <div class="maker"><span class="maker-dot"></span>Brightwell Drinks</div>
    <h1 class="product-name">TUMBLER</h1>
    <p class="tagline">MADE TO TUMBLE</p>
    <p class="flavor-note">Naturally Flavored</p>
    <p class="category">ALCOHOLIC BEVERAGE</p>
    <p class="origin">WEST VIRGINIA</p>
    <p class="volume">14% ALC/VOL · 6.9 OZ</p>
  </section>
</main>
</body>
</html>
```